Corporate travel agency website design

Hello I need a website design that will look professional. I want that anyone that gos on our site understands that we are a large successful company. I want it to be up to par with other large companies. The site should be sleek and neat.
Below I will attach my logo. A recent one page add I made and content for my add that will be used for the website.

```html
<!DOCTYPE html>
<html lang="en">
<head>
<meta charset="utf-8">
<title>Altura Travel — Business Travel Reinvented</title>
<link href="https://fonts.googleapis.com/css2?family=Poppins:wght@400;500;600;700&display=swap" rel="stylesheet">
<style>
:root{
  --navy:#061a3a;
  --navy-deep:#041230;
  --sky:#cdeffa;
  --sky-line:#bfe6f6;
  --blue:#1a8fd0;
  --ink:#1c2230;
  --body:#3a3f4a;
  --grey-bg:#f5f5f5;
  --dot:#6b7280;
  --white:#ffffff;
}
*{margin:0;padding:0;box-sizing:border-box}
html,body{width:1200px;height:3611px;overflow:hidden}
body{position:relative;background:var(--white);font-family:'Poppins',sans-serif;color:var(--body)}
.abs{position:absolute}

/* header */
.brand{left:72px;top:60px;width:220px;text-align:center}
.brand-mark{display:block;width:14px;height:14px;border-radius:50%;background:var(--navy);margin:0 auto 14px}
.brand-name{font-size:19px;letter-spacing:2px;color:var(--navy);font-weight:400}
.brand-tag{font-size:7.5px;letter-spacing:4px;color:var(--navy);margin-top:2px}
.nav{top:48px;right:74px;display:flex;gap:39px;font-weight:600;font-size:19px;color:#3b4150}
.nav .active{color:var(--navy)}

/* hero */
.hero-art{left:0;top:117px}
.hero-copy{left:75px;top:340px;color:var(--white)}
.hero-copy .pre{font-size:38px;font-weight:600;letter-spacing:.5px;line-height:1.1}
.hero-copy h1{font-size:56px;font-weight:700;letter-spacing:1px;line-height:1.05}
.hero-copy .tag{font-size:22px;margin-top:12px;font-weight:400}
.hero-copy p{font-size:19px;line-height:34px;margin-top:8px;width:420px}

/* dots */
.dots-col{width:6px;background:radial-gradient(circle,var(--dot) 1.6px,transparent 2px) 0 0/6px 22px repeat-y}
.dots-row{height:6px;background:radial-gradient(circle,var(--dot) 1.6px,transparent 2px) 0 0/22px 6px repeat-x}
.dots-grid{background:radial-gradient(circle,var(--dot) 1.6px,transparent 2px) 0 0/22px 22px}

.photo{border-radius:0}
h2.section-title{font-size:36px;font-weight:700;color:var(--navy)}
.copy{font-size:15px;line-height:27.6px;color:var(--body)}
.copy p+p{margin-top:12px}

/* services */
.services-bg{left:0;top:1490px;width:1200px;height:1588px;background:var(--grey-bg)}
.svc-icon{width:52px;height:52px;border-radius:50%;background:var(--navy);display:flex;align-items:center;justify-content:center}
.svc-head{font-size:28px;font-weight:600;color:var(--blue);line-height:35px}
.frame{background:var(--navy)}

/* network band */
.network{left:0;top:3078px;width:1200px;height:434px;background:linear-gradient(180deg,#0a1e3f 0%,#0b2a55 55%,#0d3a73 100%)}
.node-label{font-size:17px;font-weight:700;color:var(--white);line-height:28px}

/* footer */
.copyright{left:65px;top:3552px;font-size:15px;color:#3a3f4a}
.social{left:922px;top:3552px;display:flex;gap:21px}
.social span{width:22px;height:22px;border-radius:4px;background:#9aa0a8}
.scale{left:1166px;top:3560px;font-size:12px;color:#333}
</style>
</head>
<body>

<!-- header -->
<div class="abs brand">
  <span class="brand-mark"></span>
  <div class="brand-name">ALTURA TRAVEL</div>
  <div class="brand-tag">BUSINESS TRAVEL REINVENTED</div>
</div>
<nav class="abs nav">
  <span class="active">Home</span><span>About Us</span><span>Services</span><span>Why Us?</span><span>Contact Us</span>
</nav>

<!-- hero -->
<svg class="abs hero-art" width="1200" height="673" viewBox="0 117 1200 673">
  <rect x="0" y="150" width="1200" height="607" fill="#061a3a"/>
  <polygon points="676,117 1200,117 1200,789 676,789 525,450" fill="#cdeffa"/>
  <polygon points="690,117 1200,117 1200,789 690,789 540,450" fill="#8e9bb0" role="img" aria-label="Photo of business travellers walking through an airport terminal with rolling luggage"/>
  <defs><linearGradient id="heroPhoto" x1="0" x2="1" y1="0" y2="1"><stop offset="0" stop-color="#b8c3d2"/><stop offset=".5" stop-color="#6b7a92"/><stop offset="1" stop-color="#2d3a55"/></linearGradient></defs>
  <polygon points="690,117 1200,117 1200,789 690,789 540,450" fill="url(#heroPhoto)"/>
</svg>
<div class="abs hero-copy">
  <div class="pre">WELCOME TO</div>
  <h1>ALTURA TRAVEL</h1>
  <div class="tag">BUSINESS TRAVEL REINVENTED</div>
  <p>Altura Travel, We're your corporate travel partner to help you manage it all.</p>
</div>

<!-- why choose -->
<svg class="abs" style="left:0;top:789px" width="345" height="624">
  <polygon points="0,0 341,0 320,77 320,546 341,623 0,623" fill="#cdeffa"/>
</svg>
<div class="abs dots-grid" style="left:42px;top:832px;width:140px;height:44px"></div>
<div class="abs dots-col" style="left:42px;top:876px;height:78px"></div>
<div class="abs dots-col" style="left:64px;top:876px;height:78px"></div>
<div class="abs photo" role="img" aria-label="Photo of a businessman working on a laptop in an airplane seat" style="left:75px;top:866px;width:512px;height:469px;background:linear-gradient(135deg,#eef1f4 0%,#c9d0d8 45%,#6c7c92 100%)"></div>
<div class="abs dots-col" style="left:598px;top:1236px;height:110px"></div>
<div class="abs dots-row" style="left:464px;top:1349px;width:150px"></div>
<h2 class="abs section-title" style="left:617px;top:864px">Why Choose Altura Travel?</h2>
<div class="abs copy" style="left:616px;top:924px;width:516px">
  <p>Altura Travel is a global leader in business travel management services. We drive savings, efficiency, and unparalleled service to businesses and their travelers all around the world. If you are looking for a tailored travel managed solution focused on offering white glove service and fulfilling your individual preferences ,while delivering customer excellence, you've come to the right place.</p>
  <p>At Altura Travel, our mission is to have you focus on your day to day business while we handle all of the logistics and details for the most successful all encompassing travel experience. From emergency passport arrangements to last minute cancellations, re-bookings, and other intricate travel challenges, Altura Travel is well versed in handling the routine array of travel services, as well as solving any travel related issue that might arise.</p>
</div>

<!-- services -->
<div class="abs services-bg"></div>
<h2 class="abs section-title" style="left:0;width:1234px;text-align:center;top:1566px">Travel Management Services</h2>

<!-- block 1 -->
<div class="abs frame" style="left:988px;top:1651px;width:138px;height:137px"></div>
<div class="abs photo" role="img" aria-label="Photo of a traveller pulling a black suitcase through a bright terminal" style="left:613px;top:1666px;width:499px;height:368px;background:linear-gradient(160deg,#e8ecef 0%,#b7c0c8 50%,#5c6876 100%)"></div>
<div class="abs dots-col" style="left:596px;top:1932px;height:100px"></div>
<div class="abs dots-row" style="left:596px;top:2042px;width:140px"></div>
<div class="abs svc-icon" style="left:75px;top:1733px">
  <svg width="22" height="14" viewBox="0 0 22 14"><rect x="1" y="1" width="20" height="12" rx="2" fill="none" stroke="#fff" stroke-width="2"/><circle cx="11" cy="7" r="2.6" fill="#fff"/></svg>
</div>
<div class="abs svc-head" style="left:136px;top:1740px">Unparalled Service</div>
<div class="abs copy" style="left:75px;top:1804px;width:510px">
  <p>Altura Travel is famous for our concierge style approach to travel. From detailed planning, to commercial or private air travel, transportation, including car rentals, chauffers, busses for larger groups, hotels, all styles of lodging accomodations, special event planning and more, Altura Travel is like having your own personal or corporate travel butler.</p>
</div>

<!-- block 2 -->
<div class="abs frame" style="left:61px;top:2118px;width:139px;height:137px"></div>
<div class="abs photo" role="img" aria-label="Photo of a businesswoman using a laptop in an airport waiting area" style="left:75px;top:2133px;width:499px;height:367px;background:linear-gradient(135deg,#dfe7ef 0%,#a9b8c9 45%,#3f4e64 100%)"></div>
<div class="abs dots-col" style="left:586px;top:2398px;height:104px"></div>
<div class="abs dots-row" style="left:452px;top:2510px;width:150px"></div>
<div class="abs svc-icon" style="left:617px;top:2132px">
  <svg width="18" height="16" viewBox="0 0 18 16"><path d="M1 1v14h16" fill="none" stroke="#fff" stroke-width="2"/><rect x="5" y="8" width="2.4" height="5" fill="#fff"/><rect x="9" y="5" width="2.4" height="8" fill="#fff"/><rect x="13" y="9" width="2.4" height="4" fill="#fff"/></svg>
</div>
<div class="abs svc-head" style="left:678px;top:2126px">Budget and Travel Spend<br>Reporting</div>
<div class="abs copy" style="left:617px;top:2207px;width:516px">
  <p>Having a travel management service will ensure that your company enforces corporate compliance and maintains control over travel decisions. This ensures that your employees stick to your budget, which in turn will protect your bottom line.Travel expenses can be costly. Having a savvy and experienced corporate travel manager who can access deep discounts not available to the public will ensure your travel is booked across the board at the lowest prices expenses are kept under control. Travel reporting is critical to optimizing budgets, streamlining expense reports, and recognizing key trends.</p>
</div>

<!-- block 3 -->
<div class="abs frame" style="left:988px;top:2590px;width:138px;height:137px"></div>
<div class="abs photo" role="img" aria-label="Photo of hands in a suit protecting a glowing globe and plane graphic" style="left:613px;top:2605px;width:499px;height:367px;background:radial-gradient(circle at 50% 55%,#1f6e94 0%,#123a63 40%,#0a1f3e 100%)"></div>
<div class="abs dots-col" style="left:596px;top:2870px;height:104px"></div>
<div class="abs dots-row" style="left:596px;top:2984px;width:140px"></div>
<div class="abs svc-icon" style="left:75px;top:2606px">
  <svg width="18" height="18" viewBox="0 0 18 18"><circle cx="9" cy="9" r="8" fill="#fff"/><path d="M9 4.5V9l3 2" fill="none" stroke="#061a3a" stroke-width="2"/></svg>
</div>
<div class="abs svc-head" style="left:136px;top:2612px">Efficiency</div>
<div class="abs copy" style="left:75px;top:2671px;width:514px">
  <p>Time is your most valuable tool! Our goal at Altura Travel is to have your employees' complete focus be on your core business, while having us handle all the logistics for their travel. One of the most appreciated services we offer is the management of travel headaches. Unforeseen circumstances such as cancellations, missed flights, cancelled flights, last minute bookings or changed plans, can take hours to rectify. Altura Travel handles all of these tedious repositionings expeditiously, saving your employees precious time. Give your company a competitive edge by having Altura Travel handle your team's travel arrangements.</p>
</div>

<!-- network band -->
<div class="abs network" role="img" aria-label="Background photo of business travellers silhouetted in a terminal, tinted blue"></div>
<svg class="abs" style="left:0;top:3078px" width="1200" height="533" viewBox="0 3078 1200 533">
  <circle cx="600" cy="3480" r="258" fill="none" stroke="#bfe6f6" stroke-width="2"/>
  <g fill="#0a2a52" stroke="#ffffff" stroke-width="2">
    <circle cx="600" cy="3225" r="47"/><circle cx="430" cy="3283" r="47"/><circle cx="762" cy="3283" r="47"/><circle cx="342" cy="3440" r="47"/><circle cx="861" cy="3440" r="47"/>
  </g>
  <g fill="#cdeffa">
    <circle cx="600" cy="3225" r="38"/><circle cx="430" cy="3283" r="38"/><circle cx="762" cy="3283" r="38"/><circle cx="342" cy="3440" r="38"/><circle cx="861" cy="3440" r="38"/>
  </g>
  <g fill="none" stroke="#061a3a" stroke-width="2">
    <!-- expense reports -->
    <rect x="585" y="3207" width="24" height="32" rx="2"/><path d="M590 3215h14M590 3221h10M590 3227h8"/><circle cx="612" cy="3233" r="7"/><path d="M612 3226v7h7"/>
    <!-- policy compliance -->
    <rect x="414" y="3265" width="24" height="32" rx="2"/><path d="M419 3273h14M419 3279h10"/><path d="M437 3282l8 3v6c0 5-4 8-8 9-4-1-8-4-8-9v-6z"/><path d="M433 3291l3 3 5-5"/>
    <!-- full service -->
    <rect x="752" y="3267" width="26" height="17" rx="1"/><path d="M744 3290h36M748 3290v10M776 3290v10"/><circle cx="749" cy="3273" r="3"/><path d="M744 3286c0-6 10-6 10 0"/>
    <!-- white glove -->
    <path d="M330 3458v-18l-4-10c-1-3 3-5 5-2l4 8v-16c0-3 4-3 4 0v12-16c0-3 4-3 4 0v16-13c0-3 4-3 4 0v14-10c0-3 4-3 4 0v20c0 8-4 15-12 15z"/>
    <!-- savings -->
    <circle cx="862" cy="3428" r="9"/><path d="M862 3422v12M859 3425h5a2 2 0 010 4h-4a2 2 0 000 4h5"/><path d="M844 3450h6l6-4h12c3 0 3 4 0 4h-8m8 0l10-6c3-2 5 2 3 4l-12 8h-17"/>
  </g>
</svg>
<div class="abs node-label" style="left:0;width:1200px;text-align:center;top:3128px">Streamlined Expense Reports</div>
<div class="abs node-label" style="right:833px;top:3268px;text-align:right">Altura Policy Compliance</div>
<div class="abs node-label" style="left:831px;top:3248px">Full Service Travel<br>Management Program</div>
<div class="abs node-label" style="right:919px;top:3426px;text-align:right">White Glove Service</div>
<div class="abs node-label" style="left:931px;top:3426px">Unparallel Savings</div>

<!-- footer -->
<div class="abs copyright">Copyright 2023 © Altura Travel.All rights reserved</div>
<div class="abs social" aria-label="Social media links">
  <span></span><span></span><span></span><span></span><span></span>
</div>
<div class="abs scale">x10</div>

</body>
</html>
```